Startup company business card (Media & Advertising)

we need a business card design for a company that is a startup in the media and aggregation industry. Card needs to look funky and of a new breed/modern and upmarket.

Target Market(s)

advertisers/ brand agencies & media publishers

Industry/Entity Type

Advertising

Contact Information for Business Card

Please ensure the front face signifies our brand (plumvexo.com) and back has details for the contact. Standard contact such as phone , address, email , website etc.

Font styles to use
Other font styles liked:
• use styleguide and logo font and color

Colors

Designer to choose colors to be used in the design.

Requirements
Must have
• We are disrupting the media and agency industry so subtlety would be good to use imagery to signify this
Nice to have
• Please use logo colors for branding
Should not have
• be as creative and provide few options. Pick a brand color from logo and styleguide

```html
<!DOCTYPE html>
<html lang="en">
<head>
<meta charset="utf-8">
<title>Plumvexo Business Card</title>
<link href="https://fonts.googleapis.com/css2?family=Arimo:wght@400;700&display=swap" rel="stylesheet">
<style>
  :root {
    --bg: #e9e7e4;
    --card: #ffffff;
    --red: #e23344;
    --red-deep: #a31b45;
    --ink: #1a1a1a;
    --shadow: rgba(40, 20, 20, 0.22);
  }
  html, body {
    margin: 0;
    padding: 0;
    width: 1200px;
    height: 835px;
    overflow: hidden;
    background: var(--bg);
    font-family: "Arimo", Arial, sans-serif;
  }
  .canvas {
    position: relative;
    width: 1200px;
    height: 835px;
  }
  .card {
    position: absolute;
    top: 263px;
    width: 540px;
    height: 309px;
    background: var(--card);
    border-radius: 22px;
    overflow: hidden;
    box-shadow: 0 10px 26px var(--shadow);
  }
  .card--front { left: 40px; }
  .card--back { left: 620px; }
  .card-band {
    position: absolute;
    inset: 0;
    width: 100%;
    height: 100%;
  }
  .brand {
    position: absolute;
    display: flex;
    align-items: center;
    gap: 12px;
    color: var(--ink);
    font-weight: 700;
    letter-spacing: 0.5px;
  }
  .brand-dot {
    width: 26px;
    height: 26px;
    border-radius: 50%;
    background: var(--red);
  }
  .card--front .brand {
    left: 150px;
    top: 92px;
    font-size: 40px;
  }
  .card--back .brand {
    left: 32px;
    top: 60px;
    font-size: 30px;
  }
  .card--back .brand-dot { width: 22px; height: 22px; }
  .person {
    position: absolute;
    right: 30px;
    top: 26px;
    text-align: right;
  }
  .person-name {
    color: var(--red);
    font-weight: 700;
    font-size: 22px;
    letter-spacing: 1px;
  }
  .person-title {
    color: var(--ink);
    font-size: 15px;
    margin-top: 2px;
  }
  .contact {
    position: absolute;
    list-style: none;
    margin: 0;
    padding: 0;
    font-size: 15px;
    color: var(--ink);
  }
  .contact li {
    display: flex;
    align-items: center;
    gap: 10px;
    height: 24px;
  }
  .contact--left { left: 32px; top: 150px; }
  .contact--right { right: 30px; top: 126px; }
  .contact--right li { justify-content: flex-end; }
  .contact--right li .icon { order: 2; }
  .icon {
    width: 18px;
    height: 18px;
    flex: none;
  }
</style>
</head>
<body>
<main class="canvas">

  <section class="card card--front" aria-label="Card front">
    <svg class="card-band" viewBox="0 0 540 309" preserveAspectRatio="none" aria-hidden="true">
      <defs>
        <linearGradient id="bandFront" x1="0" y1="0" x2="1" y2="0">
          <stop offset="0" stop-color="#e23344"/>
          <stop offset="1" stop-color="#a31b45"/>
        </linearGradient>
      </defs>
      <path d="M0,222 C200,212 400,160 540,74 L540,309 L0,309 Z" fill="url(#bandFront)"/>
      <path d="M0,262 C220,248 420,190 540,122" fill="none" stroke="#ffffff" stroke-width="1.4"/>
    </svg>
    <div class="brand"><span class="brand-dot"></span>Plumvexo</div>
  </section>

  <section class="card card--back" aria-label="Card back">
    <svg class="card-band" viewBox="0 0 540 309" preserveAspectRatio="none" aria-hidden="true">
      <defs>
        <linearGradient id="bandBack" x1="0" y1="0" x2="1" y2="0">
          <stop offset="0" stop-color="#e23344"/>
          <stop offset="1" stop-color="#a31b45"/>
        </linearGradient>
      </defs>
      <line x1="0" y1="122" x2="540" y2="108" stroke="#a31b45" stroke-width="1.6"/>
      <line x1="0" y1="140" x2="22" y2="140" stroke="#a31b45" stroke-width="1.6"/>
      <path d="M0,255 C210,246 410,200 540,140 L540,309 L0,309 Z" fill="url(#bandBack)"/>
      <path d="M0,285 C230,272 420,226 540,172" fill="none" stroke="#ffffff" stroke-width="1.4"/>
    </svg>

    <div class="brand"><span class="brand-dot"></span>Plumvexo</div>

    <div class="person">
      <div class="person-name">Mara Quillon</div>
      <div class="person-title">Founder&amp;CEO</div>
    </div>

    <ul class="contact contact--left">
      <li>
        <svg class="icon" viewBox="0 0 20 20" aria-hidden="true">
          <circle cx="10" cy="10" r="9" fill="none" stroke="#e23344" stroke-width="1.6"/>
          <path d="M5.5 9.5 Q10 5 14.5 9.5 L13 11 L11.5 9.8 L8.5 9.8 L7 11 Z M7 11.5 H13 V14 H7 Z" fill="#e23344"/>
        </svg>
        <span>00-000-0000</span>
      </li>
      <li>
        <svg class="icon" viewBox="0 0 20 20" aria-hidden="true">
          <circle cx="10" cy="10" r="9" fill="none" stroke="#e23344" stroke-width="1.6"/>
          <rect x="5" y="6.5" width="10" height="7" fill="#e23344"/>
          <path d="M5 6.5 L10 10.5 L15 6.5" fill="none" stroke="#ffffff" stroke-width="1"/>
        </svg>
        <span>info@yourdomain.com</span>
      </li>
    </ul>

    <ul class="contact contact--right">
      <li>
        <svg class="icon" viewBox="0 0 20 20" aria-hidden="true">
          <circle cx="10" cy="10" r="9" fill="none" stroke="#e23344" stroke-width="1.6"/>
          <circle cx="10" cy="10" r="5" fill="none" stroke="#e23344" stroke-width="1.4"/>
          <path d="M5 10 H15 M10 5 Q7 10 10 15 M10 5 Q13 10 10 15" fill="none" stroke="#e23344" stroke-width="1"/>
        </svg>
        <span>www.plumvexo.com</span>
      </li>
      <li>
        <svg class="icon" viewBox="0 0 20 20" aria-hidden="true">
          <circle cx="10" cy="10" r="9" fill="none" stroke="#e23344" stroke-width="1.6"/>
          <path d="M4.5 10.5 L10 5.5 L15.5 10.5 L14 10.5 L14 14.5 L6 14.5 L6 10.5 Z" fill="#e23344"/>
        </svg>
        <span>Your Countrey Name</span>
      </li>
    </ul>
  </section>

</main>
</body>
</html>
```